Integrative Family Medicine Brochure needed

Looking for a very professional, clean, simple, minimalist, bold well designed brochure.
I am reestablishing my practice in a new town and looking for a new look. I am currently in the process of revising my corporate identity. I recently changed the business name to Brookvale Family Medicine.
You can visit the website http://brookvalefmclinic.example/ to get a feel for what I may be looking for. In the brochure I basically want excerpts from my home page, about, services and contact pages.
I have recently used Pixorama for both logo and business card and have been very happy, as soon as designs start being submitted I will switch to guaranteed payment.
"Brookvale" - similar font to "Cambria" and for "Family medicine" is "Trajan Pro"
I have attached several examples of brochures that have caught my eye to get the creative process started, but I am open to any design that conveys natural, life, health, and wellness.
Ideally colors would be muted or cool with emphasis on blues and greens
Feel free to use example stock photos in your design. I have attached the stock photos I have already purchased for the website.
Reason: Still waiting on a few more submissions, now that payment is guaranteed.
Target Market(s)
Health conscious people of all ages looking for a family medicine doctor
Industry/Entity Type
Town
Look and feel

```html
<!DOCTYPE html>
<html lang="en">
<head>
<meta charset="utf-8">
<title>Brookvale Family Medicine – Trifold Brochure</title>
<link href="https://fonts.googleapis.com/css2?family=Caladea:wght@400;700&family=Cinzel:wght@400&family=Crimson+Text:ital@0;1&display=swap" rel="stylesheet">
<style>
  :root {
    --page-bg: #ffffff;
    --paper: #f7f7f7;
    --paper-shade: #e6e6e6;
    --brand-blue: #1f6e9c;
    --brand-green: #5a9e2f;
    --band-green: #8fc06a;
    --band-green-soft: #d9ecc9;
    --text-grey: #8a8a8a;
    --text-dark: #1e1e1e;
    --photo-warm: #a9a39e;
    --photo-blue: #3d63b8;
  }
  * { box-sizing: border-box; margin: 0; padding: 0; }
  html, body { width: 1200px; height: 900px; overflow: hidden; background: var(--page-bg); }

  .brochure {
    position: absolute; left: 105px; top: 90px;
    width: 990px; height: 720px;
    display: flex;
    box-shadow: 0 2px 6px rgba(0,0,0,.18);
  }
  .panel { position: relative; width: 330px; height: 100%; overflow: hidden; }

  /* Left panel — doctor's note */
  .panel--note { background: linear-gradient(90deg, var(--paper-shade) 0%, var(--paper) 30%, #fdfdfd 100%); }
  .doctor-photo {
    position: absolute; left: 0; top: 148px; width: 153px; height: 162px;
    background: linear-gradient(180deg, var(--photo-warm) 0%, #b8b1ab 55%, var(--photo-blue) 100%);
  }
  .doctor-note {
    position: absolute; left: 70px; top: 326px; width: 232px;
    font: italic 12.4px/14.3px "Crimson Text", serif; color: var(--text-grey);
  }
  .doctor-sign {
    position: absolute; left: 178px; top: 666px;
    font: 14px "Crimson Text", serif; color: var(--text-grey);
  }

  /* Middle panel — contact */
  .panel--contact { background: linear-gradient(90deg, #f3f3f3 0%, #fbfbfb 40%, #efefef 100%); }
  .contact { position: absolute; left: 32px; top: 540px; }
  .brand-line {
    display: flex; align-items: center; gap: 6px;
    font: 700 18px "Caladea", serif; color: var(--brand-blue); margin-bottom: 6px;
  }
  .brand-dot { width: 10px; height: 10px; border-radius: 50%; background: var(--brand-green); }
  .contact p { font: 13px/17px "Crimson Text", serif; color: var(--text-dark); }
  .contact .phones { margin-top: 14px; }
  .contact .web { color: var(--brand-green); }

  /* Right panel — cover */
  .panel--cover { background: linear-gradient(180deg, #ffffff 0%, #f6f6f6 100%); }
  .cover-name {
    position: absolute; left: 0; right: 0; top: 110px; text-align: center;
    font: 700 34px/38px "Caladea", serif; color: var(--brand-blue);
  }
  .cover-sub {
    position: absolute; left: 0; right: 0; top: 152px; text-align: center;
    font: 400 15px "Cinzel", serif; letter-spacing: 2px; color: var(--brand-blue);
  }
  .cover-band {
    position: absolute; left: 0; right: 0; top: 200px; height: 300px;
    background: linear-gradient(180deg, rgba(255,255,255,0) 0%, var(--band-green-soft) 25%, var(--band-green) 55%, var(--band-green-soft) 80%, rgba(255,255,255,0) 100%);
  }
  .family-photo {
    position: absolute; left: 0; right: 0; top: 280px; height: 112px;
    background: linear-gradient(90deg, #c9d9a8 0%, #e8c9a8 35%, #d9b49a 65%, #9fbf7a 100%);
  }
  .cover-web {
    position: absolute; left: 0; right: 0; top: 410px; text-align: center;
    font: 700 15px "Crimson Text", serif; color: #ffffff;
  }
  .cover-tagline { position: absolute; left: 50px; top: 600px; display: flex; gap: 12px; align-items: flex-start; }
  .cover-doctor { font: 22px "Crimson Text", serif; color: var(--brand-blue); }
  .cover-promise { font: 15px/17px "Crimson Text", serif; color: var(--brand-green); padding-top: 6px; }
</style>
</head>
<body>
<main class="brochure">
  <section class="panel panel--note">
    <div class="doctor-photo" role="img" aria-label="Portrait photo of the doctor in blue scrubs with a stethoscope"></div>
    <p class="doctor-note">My primary purpose is to get sick people well, and the way I feel this is best done is within the framework of Integrative Family Medicine. I believe medicine is much more than just dispensing pills and I take care of each patient as I would want my own family members to be treated. Many issues face us in our goal of leading a productive healthy life. We are living longer due to the improvement in public health, nutrition, and modern medicine. Yet in many ways we have become less healthy. Obesity, cancer, heart disease, Alzheimer's, autism, are consuming the population. Much of what we suffer from is self inflicted and based in a lack of discipline. We have been tricked into valuing the momentary pleasure instead of long lasting health. Our health is an amalgam of the air we breathe, food we eat, thoughts we think, which I have heard put another way, "Health is what we do for our body minus what we do to our body."</p>
    <p class="doctor-sign">Dr. Harlow</p>
  </section>

  <section class="panel panel--contact">
    <div class="contact">
      <div class="brand-line"><span class="brand-dot"></span>Brookvale Family Medicine</div>
      <p>418 Meadowline Road<br>Fairhaven, Oregon 97402</p>
      <p class="phones">T: 555.204.7781 F: 555.204.7790</p>
      <p class="web">BrookvaleFMClinic.example</p>
    </div>
  </section>

  <section class="panel panel--cover">
    <h1 class="cover-name">Brookvale</h1>
    <p class="cover-sub">Family Medicine</p>
    <div class="cover-band"></div>
    <div class="family-photo" role="img" aria-label="Photo of a smiling family of four outdoors"></div>
    <p class="cover-web">brookvalefmclinic.example</p>
    <div class="cover-tagline">
      <span class="cover-doctor">Dr. Harlow</span>
      <span class="cover-promise">helping you<br>to live a Brookvale Life</span>
    </div>
  </section>
</main>
</body>
</html>
```